Gutschein-Design für Kost Lager
Zielgruppe
Die Kost Lager verkauft Lebensmittel mit abgelaufene MHD (Mindesthaltbarkeitsdatum), Waren aus Überproduktion ; Startup Produkte, die es nicht in den Verkauf bei den grossen Lebensmittelkonzerne wie Kaupa / Marvo und co. geschafft haben oder aus diversen Überproduktionen.
Wir haben unsere erste Filiale in Berlin NeuKöln eröffnet und unsere Kundenschaft ist bunt gemischt; von Hipstern bis konservativen Rentnern, alle lieben unser Nachhaltigkeitskonzept.
Wir bieten sehr viel Bio und Vegane Produkte an, z.B Müsli, Granola, Getreideprodukte, Brot, Getränke wie z.b Bio Mate, Chia Drinks, Bio Weine und Obst, Gemüse , Snacks und sehr viele 'unknown ' Startup Brands aus Deutschland.
Wir kaufen die Lebensmittel von den Produzenten direkt ein und prüfen diese auf Qualität.
Dadurch ist unser 'Outlet' nicht ein 'Ramsch Regal' Outlet, sondern ein Konzept mit ausgewählten Produkten für ein ausgewogenes und trendiges Lebensgefühl.
Aufgabenstellung
Food Flyer mit 50% Rabatt auf jeden Einkauf im Laden.
Vorderseite :
KOSTLAGER Logo (siehe Anhang) / NEUERÖFFNUNG und Adresse :
Öffnungszeiten : 10-20 Uhr Mo-Sa
Rückseite:
Platzhalter für 8 Bestseller mit 'normalen Preis' und im Vergleich unser reduzierter Preis . Der Apfel ist unser Rabatt Maskottchen. Sei kreativ UND Wir haben auch eine Austausch Garantie ; bei schlechter Qualität oder Defekt gibt es ein Austauschprodukt

```html
<!DOCTYPE html>
<html lang="de">
<head>
<meta charset="utf-8">
<title>Kost Lager – Neueröffnung Flyer</title>
<link rel="stylesheet" href="https://fonts.googleapis.com/css2?family=PT+Sans:wght@400;700&family=Fira+Sans+Condensed:wght@400;600;700&display=swap">
<style>
  :root {
    --stage: #dcdcdc;
    --lime: #c3d22f;
    --lime-light: #cbd845;
    --red: #c4122f;
    --red-dark: #a3152a;
    --white: #ffffff;
    --ink: #1d1d1b;
    --blush: #f6cfcf;
  }
  * { box-sizing: border-box; margin: 0; padding: 0; }
  html, body { width: 1200px; height: 589px; overflow: hidden; background: var(--stage); }
  body { position: relative; font-family: "Fira Sans Condensed", sans-serif; color: var(--ink); }

  .sheet { position: absolute; top: 92px; width: 570px; height: 404px; box-shadow: 4px 5px 8px rgba(0,0,0,.35); overflow: hidden; }

  /* Vorderseite */
  .front { left: 20px; background: var(--lime); }
  .front__headline {
    position: absolute; left: 74px; top: 40px;
    font-family: "PT Sans", sans-serif; font-weight: 700;
    font-size: 66px; letter-spacing: 1px; color: var(--red); line-height: 1;
  }
  .front__band { position: absolute; left: 0; right: 0; bottom: 0; height: 142px; background: var(--white); }
  .brand { position: absolute; left: 176px; top: 22px; display: flex; align-items: center; gap: 10px; }
  .brand__dot { width: 32px; height: 32px; border-radius: 50%; background: var(--red); }
  .brand__name { font-family: "PT Sans", sans-serif; font-weight: 700; font-size: 34px; color: var(--red); line-height: 1; }
  .front__info { position: absolute; left: 218px; top: 70px; font-family: "PT Sans", sans-serif; font-weight: 700; font-size: 10.5px; color: var(--red); line-height: 1.35; }

  /* Rückseite */
  .back { left: 610px; background: var(--lime); padding: 15px 16px 0; }
  .offers { display: grid; grid-template-columns: repeat(4, 126px); grid-auto-rows: 108px; gap: 11px; }
  .offer { position: relative; background: var(--white); border-radius: 5px; overflow: hidden; }
  .offer__photo { position: absolute; left: 5px; top: 4px; width: 90px; height: 62px; border-radius: 3px; }
  .offer__badges { position: absolute; right: 8px; top: 6px; display: flex; flex-direction: column; gap: 14px; }
  .offer__badge { width: 14px; height: 14px; border-radius: 50%; border: 2px solid var(--red); background: var(--white); }
  .offer__corner { position: absolute; right: 0; bottom: 0; width: 46px; height: 52px; background: var(--blush); clip-path: polygon(100% 0, 100% 100%, 0 100%); }
  .offer__text { position: absolute; left: 5px; bottom: 5px; width: 64px; font-size: 6px; line-height: 1.3; }
  .offer__name { font-weight: 700; font-size: 6.6px; }
  .offer__price { position: absolute; right: 5px; bottom: 5px; text-align: right; font-size: 6px; line-height: 1.1; }
  .offer__amount { display: block; margin-bottom: 1px; }
  .offer__euro { display: flex; align-items: flex-start; justify-content: flex-end; color: var(--red); font-weight: 700; }
  .offer__eur { font-size: 5.5px; margin: 7px 2px 0 0; }
  .offer__main { font-size: 17px; line-height: 1; }
  .offer__cents { font-size: 10px; line-height: 1; }
  .offer__was { display: block; font-weight: 700; margin-top: 1px; }

  .back__foot { position: absolute; left: 16px; right: 16px; bottom: 13px; display: flex; align-items: center; gap: 8px; }
  .guarantee { display: flex; align-items: center; gap: 2px; }
  .guarantee__label { background: var(--red); color: var(--white); font-weight: 700; font-size: 7px; line-height: 1; padding: 2px 4px; border-radius: 2px; }
  .guarantee__badge { width: 15px; height: 15px; border-radius: 50%; border: 2px solid var(--red); background: var(--white); }
  .back__claim { margin-left: 6px; flex: 1; color: var(--red); font-weight: 700; font-size: 7px; line-height: 1.25; }
  .back__vat { position: absolute; right: 3px; bottom: 40px; writing-mode: vertical-rl; transform: rotate(180deg); font-size: 5px; color: var(--red); }
</style>
</head>
<body>

<section class="sheet front" aria-label="Vorderseite">
  <h1 class="front__headline">NEUERÖFFNUNG</h1>
  <div class="front__band">
    <div class="brand">
      <span class="brand__dot"></span>
      <span class="brand__name">Kost Lager</span>
    </div>
    <p class="front__info">Hafenstr. 47 | 12049 Berlin<br>Öffnungszeiten: 10:00–20:00 Uhr (Mo-Sa)</p>
  </div>
</section>

<section class="sheet back" aria-label="Rückseite mit Angeboten">
  <div class="offers">
    <article class="offer">
      <div class="offer__photo" role="img" aria-label="Produktfoto: Schokoladen-Weihnachtsmänner" style="background:linear-gradient(135deg,#e7b9b9,#c4122f 55%,#2c4a8f)"></div>
      <div class="offer__badges"><span class="offer__badge"></span><span class="offer__badge"></span></div>
      <div class="offer__corner"></div>
      <p class="offer__text">Marke<br><span class="offer__name">Mais Ecken</span><br>Weihnachtsmänner aus Schokolade</p>
      <p class="offer__price"><span class="offer__amount">3 x 60 g</span><span class="offer__euro"><span class="offer__eur">EUR</span><span class="offer__main">0,</span><span class="offer__cents">79*</span></span><span class="offer__was">statt xx,xx</span></p>
    </article>
    <article class="offer">
      <div class="offer__photo" role="img" aria-label="Produktfoto: Weihnachtsdose mit Keksen und Lebkuchen" style="background:linear-gradient(135deg,#2d2d38,#8b2a2a 55%,#d9c7b0)"></div>
      <div class="offer__badges"><span class="offer__badge"></span><span class="offer__badge"></span></div>
      <div class="offer__corner"></div>
      <p class="offer__text">Marke<br><span class="offer__name">Weihnachts-Mix</span><br>1 x Weinachtskekse 340 g, 1 x Lebkuchen 125 g,</p>
      <p class="offer__price"><span class="offer__amount">465 g</span><span class="offer__euro"><span class="offer__eur">EUR</span><span class="offer__main">0,</span><span class="offer__cents">99*</span></span><span class="offer__was">statt xx,xx</span></p>
    </article>
    <article class="offer">
      <div class="offer__photo" role="img" aria-label="Produktfoto: Schokoriegel Kekse und Creme" style="background:linear-gradient(180deg,#fff 30%,#3a3f7a 30%,#1e6fb3 70%,#fff 70%)"></div>
      <div class="offer__badges"><span class="offer__badge"></span><span class="offer__badge"></span></div>
      <div class="offer__corner"></div>
      <p class="offer__text">Hollbeck<br><span class="offer__name">Cookies n Creme</span><br>Schokoladenkekse<br>Hier steht die Beschreibung</p>
      <p class="offer__price"><span class="offer__amount">125 g</span><span class="offer__euro"><span class="offer__eur">EUR</span><span class="offer__main">2,</span><span class="offer__cents">29*</span></span><span class="offer__was">statt xx,xx</span></p>
    </article>
    <article class="offer">
      <div class="offer__photo" role="img" aria-label="Produktfoto: Beutel mit Datteln in Schokolade" style="background:linear-gradient(135deg,#2b241e,#b89a6a 60%,#e8dcc4)"></div>
      <div class="offer__badges"><span class="offer__badge"></span><span class="offer__badge"></span></div>
      <div class="offer__corner"></div>
      <p class="offer__text">Marke<br><span class="offer__name">Datteln in Schokolade</span><br>Hier steht die Beschreibung</p>
      <p class="offer__price"><span class="offer__amount">3 x 100 g</span><span class="offer__euro"><span class="offer__eur">EUR</span><span class="offer__main">1,</span><span class="offer__cents">99*</span></span><span class="offer__was">statt xx,xx</span></p>
    </article>

    <article class="offer">
      <div class="offer__photo" role="img" aria-label="Produktfoto: Popcorn-Tüten" style="background:linear-gradient(90deg,#8b4fa0 50%,#f2d64b 50%)"></div>
      <div class="offer__badges"><span class="offer__badge"></span><span class="offer__badge"></span></div>
      <div class="offer__corner"></div>
      <p class="offer__text">Marke<br><span class="offer__name">Knusper Korn</span><br>Diverse Sorten z. B. Smooth Peanut &amp; Almond</p>
      <p class="offer__price"><span class="offer__amount">4 x 25 g</span><span class="offer__euro"><span class="offer__eur">EUR</span><span class="offer__main">0,</span><span class="offer__cents">49*</span></span><span class="offer__was">statt xx,xx</span></p>
    </article>
    <article class="offer">
      <div class="offer__photo" role="img" aria-label="Produktfoto: Tüten gepuffte Mais Ecken" style="background:linear-gradient(90deg,#3f9a3a 50%,#8e2a6e 50%)"></div>
      <div class="offer__badges"><span class="offer__badge"></span><span class="offer__badge"></span></div>
      <div class="offer__corner"></div>
      <p class="offer__text">bio MITTE<br><span class="offer__name">Mais Ecken</span><br>gepuffter Mais mit Hülsenfrüchten</p>
      <p class="offer__price"><span class="offer__amount">2 x 70 g</span><span class="offer__euro"><span class="offer__eur">EUR</span><span class="offer__main">0,</span><span class="offer__cents">49*</span></span><span class="offer__was">statt xx,xx</span></p>
    </article>
    <article class="offer">
      <div class="offer__photo" role="img" aria-label="Produktfoto: Dosen mit veganem Proteinshake und Aufstrich" style="background:linear-gradient(135deg,#6fae3a,#d8e6c2 50%,#2d2a2e)"></div>
      <div class="offer__badges"><span class="offer__badge"></span><span class="offer__badge"></span></div>
      <div class="offer__corner"></div>
      <p class="offer__text">grünling<br><span class="offer__name">Vegan-Mix</span><br>Protein Shake, Optus a nam que pedipie</p>
      <p class="offer__price"><span class="offer__amount">xxxx g</span><span class="offer__euro"><span class="offer__eur">EUR</span><span class="offer__main">1,</span><span class="offer__cents">99*</span></span><span class="offer__was">statt xx,xx</span></p>
    </article>
    <article class="offer">
      <div class="offer__photo" role="img" aria-label="Produktfoto: Knäckebrot und Naturreiswaffeln" style="background:linear-gradient(135deg,#d9e4ef,#2f5fa8 60%,#e9dfc8)"></div>
      <div class="offer__badges"><span class="offer__badge"></span><span class="offer__badge"></span></div>
      <div class="offer__corner"></div>
      <p class="offer__text">Marke<br><span class="offer__name">Knäckebrot + Naturreiswaffeln</span><br>Hier steht die Beschreibung</p>
      <p class="offer__price"><span class="offer__amount">2 x 200 g</span><span class="offer__euro"><span class="offer__eur">EUR</span><span class="offer__main">1,</span><span class="offer__cents">99*</span></span><span class="offer__was">statt xx,xx</span></p>
    </article>

    <article class="offer">
      <div class="offer__photo" role="img" aria-label="Produktfoto: Beutel Hartweizen-Nudeln" style="background:linear-gradient(135deg,#f1e3b8,#d6a24c 60%,#b2462f)"></div>
      <div class="offer__badges"><span class="offer__badge"></span><span class="offer__badge"></span></div>
      <div class="offer__corner"></div>
      <p class="offer__text">Teigwerk<br><span class="offer__name">Hartweizen Nudeln</span><br>Hier steht die Beschreibung</p>
      <p class="offer__price"><span class="offer__amount">2 x 500 g</span><span class="offer__euro"><span class="offer__eur">EUR</span><span class="offer__main">1,</span><span class="offer__cents">49*</span></span><span class="offer__was">statt xx,xx</span></p>
    </article>
    <article class="offer">
      <div class="offer__photo" role="img" aria-label="Produktfoto: Mehlpackungen glutenfrei" style="background:linear-gradient(180deg,#2a4f8f 25%,#cfe3f2 25%,#eef4f8)"></div>
      <div class="offer__badges"><span class="offer__badge"></span><span class="offer__badge"></span></div>
      <div class="offer__corner"></div>
      <p class="offer__text">Feldkorn<br><span class="offer__name">Mehl</span><br>Verschiedene Sorten, z. B. Bananen Mehl</p>
      <p class="offer__price"><span class="offer__amount">3 x 400 g</span><span class="offer__euro"><span class="offer__eur">EUR</span><span class="offer__main">2,</span><span class="offer__cents">98*</span></span><span class="offer__was">statt xx,xx</span></p>
    </article>
    <article class="offer">
      <div class="offer__photo" role="img" aria-label="Produktfoto: Gläser Steinpilzsauce und Pesto" style="background:linear-gradient(135deg,#e7dcc6,#2a4f8f 55%,#4e5a2a)"></div>
      <div class="offer__badges"><span class="offer__badge"></span><span class="offer__badge"></span></div>
      <div class="offer__corner"></div>
      <p class="offer__text">Feldkorn<br><span class="offer__name">Steinpilzsauce + Pesto</span><br>Hier steht die Beschreibung</p>
      <p class="offer__price"><span class="offer__amount">540 ml</span><span class="offer__euro"><span class="offer__eur">EUR</span><span class="offer__main">1,</span><span class="offer__cents">99*</span></span><span class="offer__was">statt xx,xx</span></p>
    </article>
    <article class="offer">
      <div class="offer__photo" role="img" aria-label="Produktfoto: drei Weinflaschen" style="background:linear-gradient(90deg,#2a1c22 33%,#d98b6a 33%,#d98b6a 66%,#3a1e28 66%)"></div>
      <div class="offer__badges"><span class="offer__badge"></span><span class="offer__badge"></span></div>
      <div class="offer__corner"></div>
      <p class="offer__text">Marke<br><span class="offer__name">Weine</span><br>Verschiedene Sorten, z. B. Trollinger, Dornfelder</p>
      <p class="offer__price"><span class="offer__amount">3 x 0,75 l</span><span class="offer__euro"><span class="offer__eur">EUR</span><span class="offer__main">5,</span><span class="offer__cents">98*</span></span><span class="offer__was">statt xx,xx</span></p>
    </article>
  </div>

  <div class="back__foot">
    <div class="guarantee"><span class="guarantee__label">BESTPREIS<br>GARANTIE</span><span class="guarantee__badge"></span></div>
    <div class="guarantee"><span class="guarantee__label">AUSTAUSCH<br>GARANTIE</span><span class="guarantee__badge"></span></div>
    <p class="back__claim">HIER KÖNNTE NOCH EIN KLEINER TEXT STEHEN HIER KÖNNTE NOCH EIN KLEINER TEXT STEHEN HIER KÖNNTE NOCH EIN KLEINER TEXT STEHEN HIER KÖNNTE NOCH EIN KLEINER TEXT STEHEN</p>
  </div>
  <p class="back__vat">* inkl. ges. MwSt.</p>
</section>

</body>
</html>
```